Copper Ridge Garage Door Sales & Repair needs a Business Card Design

I need a business card design to go with our new business logo that was created a few months ago.

Copper Ridge Garage Door specializes in selling and installing new garage doors, and new garage door openers. We also take care of all repairs to existing garage doors and garage door openers. All makes and models.

Target Market(s)

Home-owners, renters, anyone who lives in a house and has a garage. Residential and commercial garages.

Industry/Entity Type

Home Improvement

Contact Information for Business Card

I would like the business cards to have rounded corners and be double-sided. My old logo is still on my website at www.copperridgegarage.example. If I was going to incorporate a secondary color on the business cards, I think that orange is a good choice (especially since blue and orange are the colors of our Tulsa Kestrels), but I'm not opposed to seeing a different color if another color works better with my logo colors. I have two logo colors. One designed for a white background and one designed for a darker background. I'm not opposed to using both. Maybe a dark background with the white logo on one side, and a white background with the other logo color on the other side.

My business is a small, locally owned business that I am trying to grow. But I would like my business cards to look very professional. Like we have been in business for a long time. I like traditional to modern looking cards. Just something bold and memorable. My full company name is Copper Ridge Garage Door Sales & Repair. But you can just do COPPER RIDGE GARAGE DOOR, if that works better.

Font styles to use
Serif
Script

Requirements
Must have
• Rounded corners
• Double-sided
• 3-D Elements. Layering of some sort (a sketch of a garage door or a 3rd color (orange) brought in some how. I really like watermarks.
• Matte cards that you can write on.
• White on one side. (Or the lighter blue in my logo). Darker blue logo color on the other side.
• I would like our tag line on the cards somewhere... "For All Your Garage Door Needs".
• I would also like "Call For a FREE Estimate" by the phone number.
• And "Serving the Greater Metro Denver Area" somewhere on the card as well.
Nice to have
• Refer to "Business Card Details" above.

```html
<!DOCTYPE html>
<html lang="en">
<head>
<meta charset="utf-8">
<title>Copper Ridge Garage Doors – Business Card</title>
<link rel="stylesheet" href="https://fonts.googleapis.com/css2?family=Open+Sans:wght@400;600;700;800&display=swap">
<style>
  :root {
    --backdrop: #3a3a3c;
    --card-dark-top: #1b2233;
    --card-dark-bottom: #111622;
    --white: #ffffff;
    --navy: #3f4a72;
    --navy-text: #2f3b66;
    --orange: #f39a1e;
    --light-blue: #aebfd3;
    --ink: #2f3b66;
  }
  * { margin: 0; padding: 0; box-sizing: border-box; }
  html, body {
    width: 1200px; height: 900px; overflow: hidden;
    background: var(--backdrop);
    font-family: "Open Sans", Arial, sans-serif;
  }
  .canvas { position: relative; width: 1200px; height: 900px; }

  .card {
    position: absolute; left: 320px; width: 560px; height: 320px;
    border-radius: 22px; overflow: hidden;
    box-shadow: 0 12px 30px rgba(0,0,0,.45);
  }

  /* Dark side */
  .card-back { top: 80px; }
  .back-texture {
    position: absolute; inset: 0;
    background: linear-gradient(to bottom, var(--card-dark-top), var(--card-dark-bottom));
  }
  .back-brand {
    position: absolute; left: 0; right: 0; top: 92px;
    display: flex; align-items: center; justify-content: center; gap: 16px;
  }
  .brand-dot {
    width: 54px; height: 54px; border-radius: 50%;
    border: 3px solid var(--white);
  }
  .brand-name {
    font-weight: 800; font-size: 30px; line-height: 1.05;
    color: var(--white); text-transform: uppercase; letter-spacing: .5px;
  }
  .tagline {
    position: absolute; left: 0; right: 0; top: 215px;
    text-align: center; color: var(--white);
    font-size: 17px; font-weight: 400; letter-spacing: .6px;
  }

  /* Light side */
  .card-front { top: 500px; background: var(--white); }
  .card-front svg.band { position: absolute; inset: 0; }
  .person { position: absolute; left: 34px; top: 36px; }
  .person-name { font-size: 25px; font-weight: 700; color: var(--navy-text); letter-spacing: 1px; }
  .person-role { font-size: 14px; font-weight: 600; color: var(--orange); }

  .contact {
    position: absolute; left: 34px; top: 118px;
    font-size: 13px; font-weight: 600; color: var(--ink); line-height: 1.45;
  }
  .contact-row { display: flex; align-items: center; gap: 7px; }
  .contact-row svg { width: 11px; height: 11px; flex: none; }
  .contact-address { margin-bottom: 2px; }
  .free-note { color: var(--orange); }

  .front-brand {
    position: absolute; right: 22px; top: 42px;
    display: flex; align-items: center; gap: 10px;
    background: var(--white); padding: 8px 10px; border-radius: 8px;
  }
  .front-brand .brand-dot { width: 40px; height: 40px; border-color: var(--light-blue); }
  .front-brand .brand-name { color: var(--navy-text); font-size: 20px; }
</style>
</head>
<body>
<div class="canvas">

  <section class="card card-back" aria-label="Card back">
    <div class="back-texture" role="img" aria-label="Ribbed garage door panel texture in dark blue"></div>
    <div class="back-brand">
      <span class="brand-dot"></span>
      <span class="brand-name">Copper Ridge<br>Garage Doors</span>
    </div>
    <p class="tagline">For All Your Garage Door Needs</p>
  </section>

  <section class="card card-front" aria-label="Card front">
    <svg class="band" width="560" height="320" viewBox="0 0 560 320">
      <polygon points="0,300 560,184 560,320 0,320" fill="var(--navy)"/>
      <line x1="0" y1="291" x2="560" y2="175" stroke="var(--orange)" stroke-width="3"/>
      <text x="24" y="314" transform="rotate(-11.7 24 314)"
            fill="var(--white)" font-family="Open Sans, Arial, sans-serif"
            font-size="16" font-weight="600" letter-spacing=".4">Serving the Greater Metro Denver Area</text>
    </svg>

    <div class="person">
      <p class="person-name">EVAN COLE</p>
      <p class="person-role">Director</p>
    </div>

    <div class="contact">
      <p class="contact-address">482 Larkspur Ave<br>Westfield, CO 80000</p>
      <p class="contact-row">
        <svg viewBox="0 0 24 24"><path fill="var(--orange)" d="M6.6 10.8a15 15 0 0 0 6.6 6.6l2.2-2.2c.3-.3.7-.4 1-.2 1.1.4 2.3.6 3.6.6.6 0 1 .4 1 1V20c0 .6-.4 1-1 1A17 17 0 0 1 3 4c0-.6.4-1 1-1h3.5c.6 0 1 .4 1 1 0 1.3.2 2.5.6 3.6.1.3 0 .7-.2 1z"/></svg>
        555-014-2290 <span class="free-note">Call For a FREE Estimate</span>
      </p>
      <p class="contact-row">
        <svg viewBox="0 0 24 24"><rect x="2" y="5" width="20" height="14" rx="2" fill="none" stroke="var(--orange)" stroke-width="2.4"/><path d="M3 6l9 7 9-7" fill="none" stroke="var(--orange)" stroke-width="2.4"/></svg>
        info@copperridgegarage.example
      </p>
      <p class="contact-row">
        <svg viewBox="0 0 24 24"><circle cx="12" cy="12" r="10" fill="var(--orange)"/><path d="M2 12h20M12 2c3 3 3 17 0 20M12 2c-3 3-3 17 0 20" fill="none" stroke="var(--white)" stroke-width="1.6"/></svg>
        www.copperridgegarage.example
      </p>
    </div>

    <div class="front-brand">
      <span class="brand-dot"></span>
      <span class="brand-name">Copper Ridge<br>Garage Doors</span>
    </div>
  </section>

</div>
</body>
</html>
```